Flyer-Design für Hypnose
The designer had very good ideas! The design was completly different and absolutely convincing - great! Thank you very much!
Zielgruppe
Hypnose
Aufgabenstellung
Text Vorder- und Rückseite siehe Anlage
Auf der Vorderseite Foto und Logo (auch in der Anlage)
Farbgestaltung passend zu den Logofarben
Das Design soll kreativ und freundlich sein

```html
<!DOCTYPE html>
<html lang="de">
<head>
<meta charset="utf-8">
<title>Ruhepunkt Hypnose – Flyer</title>
<link href="https://fonts.googleapis.com/css2?family=Montserrat:wght@800;900&family=Barlow:wght@400;500;600&display=swap" rel="stylesheet">
<style>
  :root{
    --bg:#dfe6ee;
    --paper:#ffffff;
    --pink:#e8729c;
    --pink-deep:#e0608e;
    --blush:#ecc3dc;
    --lilac:#cf9fd6;
    --ink:#2a2530;
    --soft-ink:#4a4450;
    --logo-orange:#e8782a;
  }
  *{margin:0;padding:0;box-sizing:border-box}
  html,body{width:695px;height:1200px;overflow:hidden;background:var(--bg)}
  body{position:relative;font-family:'Barlow',sans-serif;color:var(--ink)}
  .page{position:absolute;left:147px;width:400px;height:566px;background:var(--paper);overflow:hidden;box-shadow:0 6px 20px rgba(40,60,90,.18)}
  .page--front{top:22px}
  .page--back{top:612px;background:linear-gradient(175deg,#ffffff 0%,#f7eef4 40%,var(--blush) 80%,#e6b0d4 100%)}

  /* front */
  .portrait{position:absolute;inset:0;background:
      linear-gradient(180deg,rgba(0,0,0,0) 55%,rgba(214,150,205,.85) 82%,var(--lilac) 100%),
      radial-gradient(ellipse at 62% 42%,#eed6d6 0%,#d9b9c6 25%,rgba(170,160,170,0) 55%),
      linear-gradient(160deg,#8b8a8c 0%,#b5a9a6 35%,#9a8e9c 65%,#b493b8 100%)}
  .brand-box{position:absolute;left:0;top:352px;width:238px;height:140px;background:rgba(255,255,255,.94);padding:22px 22px 0 28px}
  .brand{display:flex;align-items:center;gap:8px}
  .brand__dot{width:26px;height:26px;border-radius:50%;background:var(--logo-orange)}
  .brand__name{font-family:'Barlow',sans-serif;font-weight:600;font-size:26px;color:var(--logo-orange);letter-spacing:.5px}
  .brand__rule{margin:10px 0 10px;height:1px;width:150px;background:var(--logo-orange)}
  .owner{font-size:12px;line-height:1.35;color:var(--ink)}
  .address{position:absolute;right:20px;top:404px;color:#fff;font-size:9.5px;line-height:1.4;text-align:left;width:140px}
  .contact-strip{position:absolute;right:0;top:458px;width:168px;height:42px;background:#fff;padding:7px 12px;font-size:10px;line-height:1.35;color:var(--ink)}

  /* back */
  .headline{position:absolute;left:24px;top:44px;font-family:'Montserrat',sans-serif;font-weight:900;font-size:24px;line-height:1.02;color:var(--pink);text-transform:uppercase}
  .intro{position:absolute;left:24px;top:104px;width:330px;font-size:8.6px;line-height:1.4;color:var(--soft-ink)}
  .needs{position:absolute;left:24px;top:162px;list-style:none;font-size:8.6px;line-height:1.55;color:var(--soft-ink)}
  .needs li::before{content:"•";margin-right:4px;color:var(--ink)}
  .quote{position:absolute;left:198px;top:170px;width:190px;font-family:'Montserrat',sans-serif;text-transform:uppercase}
  .quote__mark{font-size:54px;line-height:.6;color:var(--pink);font-weight:900}
  .quote__mark--close{text-align:right;margin-top:4px}
  .quote__big{font-size:23px;font-weight:900;color:var(--pink);line-height:1.02}
  .quote__small{font-size:10.5px;font-weight:800;color:var(--ink);line-height:1.2}
  .quote__tag{font-family:'Barlow',sans-serif;font-size:8px;color:var(--ink);text-align:right;margin-top:2px}
  .explainer{position:absolute;left:0;bottom:0;width:230px;height:160px;background:var(--pink);color:#fff;padding:18px 20px}
  .explainer h2{font-weight:500;font-size:13px;margin-bottom:8px}
  .explainer p{font-size:8.6px;line-height:1.45}
</style>
</head>
<body>
  <section class="page page--front">
    <div class="portrait" role="img" aria-label="Porträtfoto der Hypnosetrainerin im Freien, weicher Hintergrund mit Übergang in Rosa"></div>
    <div class="brand-box">
      <div class="brand">
        <span class="brand__dot"></span>
        <span class="brand__name">ruhepunkt</span>
      </div>
      <div class="brand__rule"></div>
      <p class="owner">Mag. Lena Ostwald, BEd MSc<br>Diplomierte Hypnosetrainerin</p>
    </div>
    <p class="address">Am Lindenhang 12<br>2340 Feldau<br>https://ruhepunkt-hypnose.at</p>
    <div class="contact-strip">Kontakt: 0660/4815237<br>info@ruhepunkt-hypnose.at</div>
  </section>

  <section class="page page--back">
    <h1 class="headline">Wie Hypnose Ihr Leben<br>verändert:</h1>
    <p class="intro">Hypnose ist eine wunderbare Möglichkeit, das eigene Leben zu verbessern. Die Anwendungsbereiche sind unglaublich vielfältig – wenn einer der folgenden Punkte auf Sie zutrifft, sind Sie bei mir richtig:</p>
    <ul class="needs">
      <li>Wunsch mit dem Rauchen aufzuhören</li>
      <li>Wunsch abzunehmen</li>
      <li>Prüfungsangst/Lernblockaden</li>
      <li>Höhenangst</li>
      <li>Platzangst</li>
      <li>Flugangst</li>
      <li>Unsicherheit in Menschenmengen</li>
    </ul>
    <div class="quote">
      <div class="quote__mark">“</div>
      <div class="quote__big">Sie brauchen</div>
      <div class="quote__small">nicht daran zu glauben</div>
      <div class="quote__small">sie brauchen <span class="quote__big">es nur</span></div>
      <div class="quote__big">zuzulassen</div>
      <div class="quote__mark quote__mark--close">”</div>
      <div class="quote__tag">SIE WERDEN<br>BEGEISTERT SEIN!</div>
    </div>
    <div class="explainer">
      <h2>Was ist Hypnose?</h2>
      <p>Hypnose ist ein Zustand tiefer Entspannung, der genutzt werden kann, um erwünschte Gewohnheiten und Handlungsmuster zu verstärken oder unerwünschte aufzulösen. Zusätzlich ist Hypnose hervorragend geeignet, bei Stress oder Überforderung wieder mehr Ruhe und Wohlbefinden zu finden.</p>
    </div>
  </section>
</body>
</html>
```